Pull Up Sign for Financial Services Business

Looking to design a pull-up retractable banner for events. A design which I could add a second banner to so something that could flow across more than one banner would be ideal.

I have included my logo and business card so you can get an idea of colours and our branding style.

A disability image will be required on the banner. Dimensions are in image attached.

Target Market(s)

KAPR (Disability) Participants

Industry/Entity Type

Disability/Finance

Font styles to use
Other font styles liked:
• Raleway

Requirements
Must have
• Disability Image - match our branding. Text in image uploaded

```html
<!DOCTYPE html>
<html lang="en">
<head>
<meta charset="utf-8">
<title>Harbour Plan Services – Pull Up Banner</title>
<link href="https://fonts.googleapis.com/css2?family=Bodoni+Moda:wght@400&family=Montserrat:wght@400;600;800&family=Poppins:wght@600;700&display=swap" rel="stylesheet">
<style>
  :root{
    --stage:#d0d0d0;
    --white:#ffffff;
    --teal:#0f8a80;
    --teal-deep:#17585a;
    --magenta:#b0306a;
    --pink:#e0237a;
    --navy:#2b3a8a;
    --ink:#111111;
    --purple:#6a2a7a;
    --rule:rgba(255,255,255,.35);
  }
  *{margin:0;padding:0;box-sizing:border-box}
  html,body{width:686px;height:1200px;overflow:hidden;background:var(--stage)}
  .banner{position:absolute;left:95px;top:0;width:496px;height:1200px;background:var(--white);overflow:hidden}
  .banner-art{position:absolute;inset:0;width:100%;height:100%}
  .brand{position:absolute;top:70px;left:0;width:100%;display:flex;justify-content:center;align-items:center;gap:12px}
  .brand-square{width:52px;height:52px;background:var(--teal)}
  .brand-name{font-family:'Montserrat',sans-serif;font-weight:600;font-size:23px;line-height:1.15;color:var(--magenta)}
  .headline{position:absolute;top:676px;left:0;width:100%;text-align:center;color:var(--white)}
  .headline-serif{display:block;font-family:'Bodoni Moda',serif;font-weight:400;font-size:62px;line-height:62px;letter-spacing:1px}
  .headline-bold{display:block;font-family:'Montserrat',sans-serif;font-weight:800;font-size:64px;line-height:66px;letter-spacing:1px}
  .divider{position:absolute;top:820px;left:37px;width:423px;height:1px;background:var(--rule)}
  .divider-pill{position:absolute;top:817px;left:211px;width:74px;height:7px;border-radius:4px;background:var(--pink)}
  .tagline{position:absolute;top:835px;left:0;width:100%;text-align:center;font-family:'Montserrat',sans-serif;font-weight:400;font-size:29px;line-height:29px;color:var(--white)}
  .features{position:absolute;list-style:none;font-family:'Poppins',sans-serif;font-weight:600;font-size:13px;line-height:16px;color:var(--white)}
  .features li{position:absolute;left:0;padding-left:18px;white-space:nowrap}
  .features li::before{content:"";position:absolute;left:0;top:3px;width:11px;height:11px;border-radius:50%;background:var(--pink)}
  .features li::after{content:"";position:absolute;left:3px;top:5px;width:4px;height:2px;border-left:1.5px solid var(--white);border-bottom:1.5px solid var(--white);transform:rotate(-45deg)}
  .features-left{left:30px;top:918px}
  .features-right{left:253px;top:918px}
  .phone{position:absolute;top:1072px;left:94px;display:flex;align-items:center;gap:10px;font-family:'Poppins',sans-serif;font-weight:700;font-size:42px;line-height:46px;color:var(--white)}
  .phone-icon{width:40px;height:40px}
  .web{position:absolute;top:1119px;left:34px;display:flex;align-items:center;gap:10px}
  .partner-badge{width:52px;height:52px;border-radius:50%;background:var(--purple)}
  .web-address{font-family:'Poppins',sans-serif;font-weight:700;font-size:17.5px;color:var(--ink)}
</style>
</head>
<body>
<main class="banner">
  <svg class="banner-art" viewBox="0 0 466 1126" preserveAspectRatio="none" aria-hidden="false">
    <defs>
      <linearGradient id="band" x1="0" y1="0" x2="0" y2="1">
        <stop offset="0" stop-color="#0f8a80"/>
        <stop offset="1" stop-color="#17585a"/>
      </linearGradient>
      <linearGradient id="photoWarm" x1="0" y1="0" x2="1" y2="1">
        <stop offset="0" stop-color="#c9b59a"/>
        <stop offset="1" stop-color="#e2c45a"/>
      </linearGradient>
      <linearGradient id="photoFamily" x1="0" y1="0" x2="1" y2="1">
        <stop offset="0" stop-color="#b89a7a"/>
        <stop offset="1" stop-color="#3f5a86"/>
      </linearGradient>
      <linearGradient id="photoDesk" x1="0" y1="0" x2="1" y2="1">
        <stop offset="0" stop-color="#8aa6b8"/>
        <stop offset="1" stop-color="#2f3848"/>
      </linearGradient>
      <linearGradient id="photoAgent" x1="0" y1="0" x2="1" y2="1">
        <stop offset="0" stop-color="#5fb0ad"/>
        <stop offset="1" stop-color="#2a3f5e"/>
      </linearGradient>
    </defs>

    <!-- teal lower band -->
    <rect class="info-band" x="0" y="575" width="466" height="453" fill="url(#band)"/>

    <!-- flags -->
    <polygon role="img" aria-label="Australian flag draped at left" points="0,470 215,612 200,625 0,625" fill="var(--navy)"/>
    <polygon role="img" aria-label="Australian flag draped at right" points="466,470 251,612 266,625 466,625" fill="var(--navy)"/>

    <!-- magenta wedges -->
    <polygon class="wedge" points="0,398 228,606 228,618 0,470" fill="var(--magenta)"/>
    <polygon class="wedge" points="466,398 238,606 238,618 466,470" fill="var(--magenta)"/>
    <polygon points="233,624 0,460 0,470 233,632 466,470 466,460" fill="var(--white)"/>

    <!-- outline chevrons -->
    <polyline points="0,282 85,195 224,334" fill="none" stroke="var(--teal)" stroke-width="4"/>
    <polyline points="466,282 381,195 242,334" fill="none" stroke="var(--teal)" stroke-width="4"/>
    <polyline points="160,266 233,192 306,266" fill="none" stroke="var(--magenta)" stroke-width="3"/>

    <!-- photo diamonds -->
    <polygon role="img" aria-label="Photo of two women smiling over a laptop" points="0,294 85,208 214,338 85,466 0,382" fill="url(#photoWarm)"/>
    <polygon role="img" aria-label="Photo of a child hugging a parent in a wheelchair with family" points="466,294 381,208 252,338 381,466 466,382" fill="url(#photoFamily)"/>
    <polygon role="img" aria-label="Photo of a hand using a calculator" points="233,206 292,266 233,326 174,266" fill="url(#photoDesk)"/>
    <polygon points="233,336 374,476 233,616 92,476" fill="var(--white)"/>
    <polygon role="img" aria-label="Photo of a smiling support agent wearing a headset" points="233,346 364,476 233,606 102,476" fill="url(#photoAgent)"/>

    <!-- white footer -->
    <rect x="0" y="1028" width="466" height="98" fill="var(--white)"/>

    <!-- phone badge -->
    <polygon points="88,1006 380,1006 390,1027 380,1048 88,1048 76,1027" fill="var(--pink)"/>
  </svg>

  <header class="brand">
    <span class="brand-square"></span>
    <span class="brand-name">Harbour<br>Plan Services</span>
  </header>

  <h1 class="headline">
    <span class="headline-serif">YOUR PLAN</span>
    <span class="headline-bold">YOUR WAY</span>
  </h1>

  <div class="divider"></div>
  <div class="divider-pill"></div>

  <p class="tagline">Australia wide plan<br>management</p>

  <ul class="features features-left">
    <li style="top:0">Invoices processed daily</li>
    <li style="top:32px">Providers paid within 3<br>business days</li>
    <li style="top:79px">Expense reimbursements</li>
    <li style="top:110px">Real time funding access</li>
  </ul>
  <ul class="features features-right">
    <li style="top:0">Your own personal<br>dedicated plan manager</li>
    <li style="top:48px">Monthly statements</li>
    <li style="top:79px">Choice and control<br>use both registered and<br>unregistered providers</li>
  </ul>

  <div class="phone">
    <svg class="phone-icon" viewBox="0 0 40 40" aria-hidden="true">
      <circle cx="20" cy="20" r="18" fill="var(--white)" stroke="var(--teal)" stroke-width="3"/>
      <path d="M13 11c1-1 2.5-1 3 0l2 4c.4 .8 .2 1.6-.5 2.1l-1.5 1c1 2.4 2.6 4 5 5l1-1.5c.5-.7 1.3-.9 2.1-.5l4 2c1 .5 1 2 0 3l-1.8 1.8c-1 1-2.6 1.2-3.9.6-5.2-2.4-9-6.2-11.4-11.4-.6-1.3-.4-2.9.6-3.9z" fill="var(--ink)"/>
    </svg>
    <span class="phone-number">1300 555 018</span>
  </div>

  <footer class="web">
    <span class="partner-badge"></span>
    <span class="web-address">www.harbourplanservices.com.au</span>
  </footer>
</main>
</body>
</html>
```